International house cleaning business needs Marketing Landing Page for improving user acquisition

We are in need of an additional marketing Landing Page that we can use to test and improve our user acquisition. We will be looking at a minimum of one page selection, but are open to awarding up to 5 depending on the quality of work and the different variables to test.

Our current homepages are www.tidvane.com and https://www.tidvane.com/lps/firstnhours.aspx?c=MARKETING39&city=Toronto&gclid=CIqXg7z_wsECFUKCMgodknwAGA and we are looking for ways that will improve 1) Account Creation and 2) Appointment Bookings by making them more simple. Please look at the entire process and address the main issues in the Landing Page that you create.

Competitors include www.plumbix.com and www.nestrova.com

The design will be entirely up to your discretion, however the required aspects are below:

1) Maintain Corporate color scheme
2) Target audience are new users coming from offer based marketing campaigns
3) Will need an area of the page with a changeable 'offer message'
4) The offer area mentioned above should also be easily removable if there is no offer
5) The focus is on new users but we will still need to have a visible 'sign in button' for returning users
6) Wirpage login and create account with email CTA's both must be large and visible
7) Opt-in for eNewsletter button when email address is collected
8) We also have a short informative video so feel free to incorporate that in a version

General Ideas:

*email collection on Landing Page to start engagement early
*email and postal code collection on Landing Page to start engagement early
*general information and booking form on the HP to reduce the click needed to get to account creation or booking
*"Tell Us About Your Place" info (# of beds and # of baths) on HP to get process started (similar to www.quelmora.com)

Good Examples:

www.wirpage.com (merges info and sign-up)
www.quelmora.com (early engagement)
www.ladvo.com (early engagement)

Industry/Entity Type

Marketing

```html
<!DOCTYPE html>
<html lang="en">
<head>
<meta charset="utf-8">
<title>Tidvane – Home Cleaning</title>
<link rel="stylesheet" href="https://fonts.googleapis.com/css2?family=Open+Sans:ital,wght@0,300;0,400;0,600;0,700;1,600;1,700&family=Lora:ital@1&display=swap">
<style>
  :root {
    --teal: #1a6b7e;
    --teal-dark: #146373;
    --mint: #2bb69a;
    --coral: #ee6a5f;
    --coral-dark: #d2453b;
    --navy: #3b5898;
    --navy-dark: #2b4382;
    --ink: #444;
    --muted: #555;
    --hero-bg: #ebe9e8;
    --band-bg: #f6f6f6;
    --card-bg: #efefef;
    --white: #fff;
  }
  * { box-sizing: border-box; margin: 0; padding: 0; }
  html, body { width: 1119px; height: 1200px; overflow: hidden; }
  body { position: relative; background: var(--white); font-family: "Open Sans", Arial, sans-serif; color: var(--ink); }
  .abs { position: absolute; }

  /* Hero */
  .hero { left: 0; top: 0; width: 1119px; height: 478px; background: var(--hero-bg); }
  .logo { left: 120px; top: 32px; font-size: 34px; font-weight: 700; color: var(--coral); letter-spacing: -0.5px; }
  .nav { top: 42px; right: 120px; display: flex; align-items: center; gap: 28px; }
  .nav a { color: var(--teal); text-decoration: none; font-size: 13.5px; font-weight: 600; letter-spacing: .2px; }
  .nav a.sign-in { border: 2px solid var(--teal); border-radius: 3px; padding: 5px 14px; }
  .hero-title { left: 120px; top: 132px; width: 450px; font-size: 26px; line-height: 28px; font-weight: 600; color: var(--teal); }
  .hero-copy { left: 120px; top: 204px; width: 430px; font-size: 17px; line-height: 27px; font-weight: 400; color: var(--muted); }
  .btn { top: 300px; width: 204px; height: 52px; border-radius: 3px; color: var(--white); font-size: 19px; display: flex; align-items: center; justify-content: center; text-decoration: none; }
  .btn-quote { left: 120px; background: var(--coral); border-bottom: 4px solid var(--coral-dark); font-size: 20px; }
  .btn-wirpage { left: 344px; background: var(--navy); border-bottom: 4px solid var(--navy-dark); font-size: 18px; }

  .signup { left: 120px; top: 370px; width: 428px; display: flex; gap: 8px; }
  .signup-email { flex: 1; height: 44px; border: 1px solid #cfcccb; border-radius: 3px; background: var(--white); padding: 0 12px; font: 400 14px "Open Sans", Arial, sans-serif; color: #999; display: flex; align-items: center; }
  .signup-btn { width: 196px; height: 44px; border-radius: 3px; background: var(--mint); border-bottom: 3px solid #1f9a82; color: var(--white); font-size: 14.5px; font-weight: 600; display: flex; align-items: center; justify-content: center; text-decoration: none; }
  .optin { left: 120px; top: 426px; display: flex; align-items: center; gap: 8px; font-size: 13px; color: var(--muted); }
  .optin-box { width: 15px; height: 15px; border: 1px solid #b9b6b5; border-radius: 2px; background: var(--white); display: flex; align-items: center; justify-content: center; }

  .video { left: 569px; top: 141px; width: 431px; height: 260px; border: 2px solid #d3d3d3; overflow: hidden; }
  .video-still { position: absolute; inset: 0; background: linear-gradient(120deg, #5a4aa8 0%, #6b5bb8 35%, #c7c4c0 60%, #8b6a44 85%, #4a3a2a 100%); }
  .video-bar { position: absolute; left: 0; right: 0; bottom: 0; height: 56px; background: linear-gradient(rgba(0,0,0,0), rgba(0,0,0,.75) 40%); }
  .video-controls { position: absolute; left: 0; bottom: 0; }

  /* Offer section */
  .offer-photo { left: 120px; top: 524px; width: 430px; height: 246px; background: #dedede; padding: 7px; }
  .offer-photo-fill { width: 100%; height: 100%; background: linear-gradient(90deg, #f4f4f4 0%, #ececec 50%, #e3e6e4 70%, #4fb3a3 85%, #e9e9e9 100%); }
  .offer-badge { left: 155px; top: 542px; width: 133px; height: 133px; border-radius: 50%; background: var(--teal); color: var(--white); text-align: center; display: flex; flex-direction: column; justify-content: center; box-shadow: inset 0 0 0 6px rgba(255,255,255,.08); }
  .offer-badge .price { font-size: 28px; font-weight: 700; line-height: 32px; }
  .offer-badge .desc { font-size: 17px; font-weight: 600; line-height: 25px; }
  .pitch-title { left: 569px; top: 528px; font-size: 26px; line-height: 30px; color: var(--teal); font-weight: 400; }
  .pitch-title strong { display: block; color: var(--mint); font-weight: 700; letter-spacing: .5px; }
  .pitch-copy { left: 569px; top: 602px; width: 430px; font-size: 14px; line-height: 18px; font-weight: 300; color: var(--ink); }
  .ticks { left: 578px; top: 652px; list-style: none; }
  .ticks li { display: flex; align-items: center; gap: 10px; font-size: 18px; line-height: 27px; color: var(--ink); }

  /* Testimonials */
  .reviews { left: 0; top: 820px; width: 1119px; height: 296px; background: var(--band-bg); }
  .reviews-title { left: 0; top: 848px; width: 1119px; text-align: center; font-size: 29px; font-weight: 400; color: #3d3d3d; }
  .reviews-title em { color: var(--mint); font-weight: 700; }
  .quote-card { top: 922px; width: 217px; }
  .quote-box { position: relative; height: 82px; background: var(--card-bg); border: 1px solid #e2e2e2; border-bottom: 2px solid #9fc9d3; border-radius: 3px; padding: 12px 12px 0 32px; font-family: "Lora", Georgia, serif; font-style: italic; font-size: 9.5px; line-height: 14px; color: #666; }
  .quote-box::before { content: "\201C"; position: absolute; left: 11px; top: 4px; font-family: Georgia, serif; font-style: normal; font-weight: 700; font-size: 24px; color: var(--mint); }
  .quote-tail { position: absolute; left: 28px; top: 81px; }
  .author { display: flex; align-items: center; gap: 10px; margin: 28px 0 0 22px; font-size: 10px; color: var(--teal); }
  .author b { font-weight: 600; }
  .avatar { width: 28px; height: 28px; border-radius: 50%; background: linear-gradient(#e9d9cc, #5fb3a3); border: 2px solid #fff; box-shadow: 0 0 0 1px #ddd; }

  /* Footer */
  .footer { left: 0; top: 1116px; width: 1119px; height: 84px; background: var(--teal-dark); }
  .footer-links { left: 120px; top: 1141px; display: flex; gap: 20px; }
  .footer-links a { color: var(--white); font-size: 12px; text-decoration: none; }
  .copyright { left: 120px; top: 1168px; color: var(--white); font-size: 9.5px; }
  .socials { left: 846px; top: 1146px; display: flex; gap: 17px; }
  .socials span { width: 25px; height: 25px; border-radius: 3px; display: block; }
</style>
</head>
<body>
  <header class="abs hero"></header>
  <div class="abs logo">Tidvane.com</div>
  <nav class="abs nav">
    <a href="#">HELP</a>
    <a href="#">ABOUT US</a>
    <a href="#">STANDARD CLEANING CHECKLIST</a>
    <a class="sign-in" href="#">SIGN IN</a>
  </nav>
  <h1 class="abs hero-title">Lorem ipsum is a dummy text only dolor sit amet cons ectetur.</h1>
  <p class="abs hero-copy">Aboris nisi ut aliquip ex ea commodo consequat. Duis aute irure dolor in reprehenderit in voluptate velit esse cillum dolore eu fugiat nulla.</p>
  <a class="abs btn btn-quote" href="#">Get a Quote Now</a>
  <a class="abs btn btn-wirpage" href="#">Book with Wirpage</a>

  <form class="abs signup">
    <span class="signup-email">Your email address</span>
    <a class="signup-btn" href="#">Create Account with Email</a>
  </form>
  <label class="abs optin">
    <span class="optin-box"><svg width="11" height="9" viewBox="0 0 11 9"><path d="M1 4.5 L4 7.5 L10 1" fill="none" stroke="#2bb69a" stroke-width="2"/></svg></span>
    Yes, send me the eNewsletter with offers and tips
  </label>

  <div class="abs video">
    <div class="video-still" role="img" aria-label="Video still of a cleaner wiping an office desk"></div>
    <div class="video-bar"></div>
    <svg class="video-controls" width="431" height="56" viewBox="0 0 431 56">
      <rect x="22" y="18" width="384" height="3" fill="#222"/>
      <rect x="22" y="18" width="190" height="3" fill="#1f8fa0"/>
      <path d="M25 32 L34 37 L25 42 Z" fill="#fff"/>
      <path d="M57 33.5 a4.5 4.5 0 1 0 3 1.5" fill="none" stroke="#fff" stroke-width="1.6"/>
      <path d="M59 31 L62 34 L58 35 Z" fill="#fff"/>
      <text x="67" y="41" fill="#fff" font-family="Open Sans, sans-serif" font-size="11" font-weight="700">3:19 / 7:00</text>
      <path d="M275 34 h3 l4 -3 v12 l-4 -3 h-3 Z" fill="#fff"/>
      <path d="M284 34 l4 4 M288 34 l-4 4" stroke="#fff" stroke-width="1.2"/>
      <rect x="294" y="36" width="70" height="2" fill="#444"/>
      <rect x="294" y="36" width="42" height="2" fill="#fff"/>
      <path d="M377 34 h3 l4 -3 v12 l-4 -3 h-3 Z" fill="#fff"/>
      <path d="M386 34 v6 M389 32 v10" stroke="#fff" stroke-width="1.2"/>
      <path d="M397 32 l3 3 M404 32 l-3 3 M397 43 l3 -3 M404 43 l-3 -3" stroke="#fff" stroke-width="1.8"/>
    </svg>
  </div>

  <div class="abs offer-photo"><div class="offer-photo-fill" role="img" aria-label="Photo of a smiling cleaner holding a mop and bucket in a bright room"></div></div>
  <div class="abs offer-badge">
    <div class="price">$39</div>
    <div class="desc">Cleaning for<br>3 Hours</div>
  </div>
  <h2 class="abs pitch-title">Do you really have the time to clean <strong>YOUR HOME?</strong></h2>
  <p class="abs pitch-copy">Give your home a fresh, thorough cleaning by Tidvane professionals. Just schedule when and we'll do the rest!</p>
  <ul class="abs ticks">
    <li><svg width="15" height="13" viewBox="0 0 15 13"><path d="M1 7 L5 11 L14 2" fill="none" stroke="#2bb69a" stroke-width="3"/></svg>Fully screened cleaners</li>
    <li><svg width="15" height="13" viewBox="0 0 15 13"><path d="M1 7 L5 11 L14 2" fill="none" stroke="#2bb69a" stroke-width="3"/></svg>60-point checklist</li>
    <li><svg width="15" height="13" viewBox="0 0 15 13"><path d="M1 7 L5 11 L14 2" fill="none" stroke="#2bb69a" stroke-width="3"/></svg>Friendly client services</li>
    <li><svg width="15" height="13" viewBox="0 0 15 13"><path d="M1 7 L5 11 L14 2" fill="none" stroke="#2bb69a" stroke-width="3"/></svg>Satisfaction assured</li>
  </ul>

  <section class="abs reviews"></section>
  <h2 class="abs reviews-title">What our Customers <em>Say</em></h2>

  <div class="abs quote-card" style="left:153px">
    <div class="quote-box">Lorem ipsum dolor sit amet, consec tetur adipisicing elit, sed do eiusmod tempor incididunt ut labore.
      <svg class="quote-tail" width="30" height="17" viewBox="0 0 30 17"><path d="M0 0 L15 16 L30 0" fill="#efefef" stroke="#9fc9d3" stroke-width="2"/><rect x="2" y="-2" width="26" height="2" fill="#efefef"/></svg>
    </div>
    <div class="author"><span class="avatar" role="img" aria-label="Customer portrait"></span><span><b>Jenny Smith</b>, New York</span></div>
  </div>
  <div class="abs quote-card" style="left:451px">
    <div class="quote-box">Lorem ipsum dolor sit amet, consec tetur adipisicing elit, sed do eiusmod tempor incididunt ut labore.
      <svg class="quote-tail" width="30" height="17" viewBox="0 0 30 17"><path d="M0 0 L15 16 L30 0" fill="#efefef" stroke="#9fc9d3" stroke-width="2"/><rect x="2" y="-2" width="26" height="2" fill="#efefef"/></svg>
    </div>
    <div class="author"><span class="avatar" role="img" aria-label="Customer portrait"></span><span><b>Natalie Jordan</b>, Los Angeles</span></div>
  </div>
  <div class="abs quote-card" style="left:750px">
    <div class="quote-box">Lorem ipsum dolor sit amet, consec tetur adipisicing elit, sed do eiusmod tempor incididunt ut labore.
      <svg class="quote-tail" width="30" height="17" viewBox="0 0 30 17"><path d="M0 0 L15 16 L30 0" fill="#efefef" stroke="#9fc9d3" stroke-width="2"/><rect x="2" y="-2" width="26" height="2" fill="#efefef"/></svg>
    </div>
    <div class="author"><span class="avatar" role="img" aria-label="Customer portrait"></span><span><b>Jenny Smith</b>, New York</span></div>
  </div>

  <footer class="abs footer"></footer>
  <nav class="abs footer-links">
    <a href="#">Standard Cleaning Checklist</a>
    <a href="#">About Us</a>
    <a href="#">Terms Of Use</a>
    <a href="#">Privacy Policy</a>
  </nav>
  <p class="abs copyright">Copyright©tidvane.com 2014. All Rights Reserved</p>
  <div class="abs socials" aria-label="Social links">
    <span style="background:#3b5898"></span>
    <span style="background:#2aa7dd"></span>
    <span style="background:#3a3a3a"></span>
    <span style="background:#c4302b"></span>
  </div>
</body>
</html>
```